Online Psychology Practice needs business cards.

Online Psychology service needs business cards. Have own logo- please see uploaded. I have other file formats if you need (not sure one needed?)

Details for Business Card:
Helena Marchetti
Clinical Psychologist BPsych, BPsych (Hons), MPsych (Clin), MAPS
T: 0439627015 | F: 08 73615204
E: hello@brightwatertelehealthcounselling.com.au
W: brightwatertelehealthcounselling.com.au

Industry/Entity Type

Health

Contact Information for Business Card

Logo plus details above (couldn't write in this section)

```html
<!DOCTYPE html>
<html lang="en">
<head>
<meta charset="utf-8">
<title>Brightwater Telehealth Counselling — Business Cards</title>
<link rel="stylesheet" href="https://fonts.googleapis.com/css2?family=Cinzel:wght@600;700&family=Roboto+Condensed:wght@400&display=swap">
<style>
  :root {
    --backdrop: #3b3b3d;
    --card-white: #ffffff;
    --navy: #1c5880;
    --teal: #1a93b0;
    --ink-grey: #555a60;
    --back-blue: #1a5c84;
    --back-blue-deep: #124a6c;
    --rule-light: #e8f1f6;
  }
  * { box-sizing: border-box; margin: 0; padding: 0; }
  html, body {
    width: 1200px; height: 900px; overflow: hidden;
    background: var(--backdrop);
  }
  .canvas {
    position: relative; width: 1200px; height: 900px;
    display: flex; align-items: center; justify-content: center; gap: 60px;
  }
  .card {
    position: relative; width: 500px; height: 286px;
    border-radius: 18px; overflow: hidden;
    box-shadow: 0 14px 30px rgba(0,0,0,0.35);
  }

  /* Front */
  .card--front { background: var(--card-white); }
  .brand {
    position: absolute; left: 30px; top: 24px;
  }
  .brand__rule {
    display: block; width: 210px; height: 2px; background: var(--teal); margin-bottom: 6px;
  }
  .brand__name {
    font-family: "Cinzel", serif; font-weight: 700; font-size: 17px;
    line-height: 1.2; letter-spacing: 1.5px; color: var(--navy);
  }
  .brand__name span { display: block; }
  .accent-bar {
    position: absolute; left: 0; top: 96px; width: 8px; height: 28px; background: var(--teal);
  }
  .person {
    position: absolute; left: 30px; top: 98px;
  }
  .person__name {
    font-family: "Cinzel", serif; font-weight: 700; font-size: 22px;
    color: var(--navy); letter-spacing: 0.5px;
  }
  .person__role {
    margin-top: 4px;
    font-family: "Roboto Condensed", sans-serif; font-size: 12.5px; line-height: 1.35;
    color: var(--ink-grey);
  }
  .contact {
    position: absolute; left: 30px; top: 178px; list-style: none;
    font-family: "Roboto Condensed", sans-serif; font-size: 12px; line-height: 1.45;
    color: var(--ink-grey);
  }
  .contact li { display: flex; align-items: center; gap: 6px; }
  .contact svg { width: 10px; height: 10px; fill: var(--navy); flex: none; }
  .feature-mark {
    position: absolute; right: -20px; bottom: -20px; width: 210px; height: 190px;
    border-radius: 60px 0 0 0;
    background: linear-gradient(135deg, var(--teal), var(--navy));
  }

  /* Back */
  .card--back {
    background: radial-gradient(circle at 45% 45%, var(--back-blue), var(--back-blue-deep));
    display: flex; align-items: center; justify-content: center;
  }
  .back-brand { text-align: center; }
  .back-brand__rule {
    display: block; width: 300px; height: 2px; background: var(--rule-light); margin: 0 auto 12px;
  }
  .back-brand__rule--end { margin: 12px auto 0; }
  .back-brand__name {
    font-family: "Cinzel", serif; font-weight: 700; font-size: 28px;
    line-height: 1.25; letter-spacing: 2px; color: var(--card-white);
  }
  .back-brand__name span { display: block; }
</style>
</head>
<body>
<main class="canvas">

  <section class="card card--front" aria-label="Business card front">
    <div class="brand">
      <span class="brand__rule"></span>
      <p class="brand__name"><span>BRIGHTWATER</span><span>TELEHEALTH COUNSELLING</span></p>
    </div>

    <span class="accent-bar"></span>
    <div class="person">
      <h1 class="person__name">HELENA MARCHETTI</h1>
      <p class="person__role">Clinical Psychologist BPsych,<br>BPsych (Hons), MPsych (Clin), MAPS</p>
    </div>

    <ul class="contact">
      <li>
        <svg viewBox="0 0 10 10" aria-hidden="true"><path d="M2 0.5 L3.8 2.6 L2.9 3.7 Q4 6 6.3 7.1 L7.4 6.2 L9.5 8 L8.4 9.5 Q3.5 9 0.5 1.6 Z"/></svg>
        0439627015
      </li>
      <li>
        <svg viewBox="0 0 10 10" aria-hidden="true"><rect x="2.5" y="0.5" width="5" height="3"/><rect x="0.5" y="3.5" width="9" height="4" rx="1"/><rect x="2.5" y="6.5" width="5" height="3"/></svg>
        08 73615204
      </li>
      <li>
        <svg viewBox="0 0 10 10" aria-hidden="true"><path d="M0.5 2 H9.5 V8 H0.5 Z M1 2.4 L5 5.4 L9 2.4" stroke="#fff" stroke-width="0.8"/></svg>
        hello@brightwatertelehealthcounselling.com.au
      </li>
      <li>
        <svg viewBox="0 0 10 10" aria-hidden="true"><circle cx="5" cy="5" r="4.5"/><path d="M0.5 5 H9.5 M5 0.5 Q2 5 5 9.5 M5 0.5 Q8 5 5 9.5" stroke="#fff" stroke-width="0.7" fill="none"/></svg>
        www.brightwatertelehealthcounselling.com.au
      </li>
    </ul>

    <div class="feature-mark" role="img" aria-label="Large brand symbol in navy and teal"></div>
  </section>

  <section class="card card--back" aria-label="Business card back">
    <div class="back-brand">
      <span class="back-brand__rule"></span>
      <p class="back-brand__name"><span>BRIGHTWATER</span><span>TELEHEALTH</span><span>COUNSELLING</span></p>
      <span class="back-brand__rule back-brand__rule--end"></span>
    </div>
  </section>

</main>
</body>
</html>
```